Business Card, Letterhead, Envelopes, Thank you cards, Post Cards
Business cards and stationary for life coach
Professional
Silver Heron Guidance Studio
Marla Penrick, MA
4810 North Calloway Avenue
Suite C 240
Missoula, Montana 59417
silverheronguidance@mailbox-example.net
silverheronguidance-example.com
I would like to see 'Let Your Dreams Take Flight' on the front of the card. This is the tagline. Please use a compatible font with the logo.
'Dragonfly spends most of her life underwater until the day she discovers her wings and soars upon the wind.' I'd like to see this in script, similar to the logo font.
Please let me know if you need different files.

```html
<!DOCTYPE html>
<html lang="en">
<head>
<meta charset="utf-8">
<title>Silver Heron Guidance Studio – Stationery Set</title>
<link rel="stylesheet" href="https://fonts.googleapis.com/css2?family=Open+Sans:wght@400;600&family=Great+Vibes&display=swap">
<style>
  :root {
    --stage: #e9e6df;
    --paper: #ffffff;
    --blue-deep: #0b4f9c;
    --blue-mid: #1f7fd1;
    --blue-light: #7fc0ef;
    --blue-pale: #d8ecfa;
    --ink: #3a4a5c;
    --label: #6a5a40;
    --line: #b9c6d3;
  }
  * { box-sizing: border-box; margin: 0; padding: 0; }
  html, body { width: 1200px; height: 391px; overflow: hidden; }
  body { background: var(--stage); font-family: "Open Sans", sans-serif; color: var(--ink); position: relative; }
  .piece { position: absolute; background: var(--paper); box-shadow: 0 1px 3px rgba(0,0,0,.25); overflow: hidden; }
  .piece--blue { background: linear-gradient(160deg, var(--blue-mid), var(--blue-deep)); color: #fff; }
  .label { position: absolute; font-size: 5px; color: var(--label); text-align: center; width: 100%; top: -8px; left: 0; }
  .holder { position: absolute; }
  .wave { position: absolute; left: 0; bottom: 0; width: 100%; }
  .brand { display: flex; align-items: center; gap: 3px; font-weight: 600; color: var(--blue-mid); line-height: 1.1; }
  .brand__dot { width: 8px; height: 8px; border-radius: 50%; background: var(--blue-light); flex: none; }
  .brand--white { color: #fff; }
  .brand--white .brand__dot { background: rgba(255,255,255,.6); }
  .small { font-size: 4px; line-height: 1.5; }
  .footer { position: absolute; right: 8px; bottom: 6px; text-align: right; color: #fff; font-size: 4px; line-height: 1.5; z-index: 2; }
  .form { position: absolute; left: 14px; top: 56px; width: 150px; border: 0.6px solid var(--line); }
  .form__row { height: 12px; border-bottom: 0.6px solid var(--line); font-size: 4.5px; padding: 3px 4px; }
  .form__row:last-child { border-bottom: none; }
  .checks { position: absolute; left: 14px; top: 112px; display: flex; gap: 10px; font-size: 4px; }
  .checks span::before { content: ""; display: inline-block; width: 4px; height: 4px; border: .5px solid var(--ink); margin-right: 2px; vertical-align: middle; }
  .tagline { font-size: 5px; font-style: italic; }
  .script { font-family: "Great Vibes", cursive; }
  .postlines { position: absolute; right: 10px; top: 40px; width: 60px; }
  .postlines i { display: block; border-bottom: .6px solid var(--line); height: 10px; }
  .stamp { position: absolute; right: 10px; top: 8px; width: 14px; height: 16px; border: .6px dashed var(--line); }
  .divider { position: absolute; left: 50%; top: 10px; bottom: 24px; border-left: .6px solid var(--line); }
  .flap { position: absolute; left: 0; top: 0; width: 100%; height: 60%; }
</style>
</head>
<body>

<!-- Letterhead with intake form -->
<div class="holder" style="left:19px;top:14px;width:235px;height:358px;">
  <div class="label">Letterhead</div>
  <section class="piece" style="inset:0;">
    <div class="brand" style="position:absolute;left:14px;top:18px;font-size:8px;"><span class="brand__dot"></span>Silver Heron<br>Guidance Studio</div>
    <div class="form">
      <div class="form__row">Name</div>
      <div class="form__row">Date</div>
      <div class="form__row">Goal</div>
      <div class="form__row">Notes</div>
    </div>
    <div class="checks"><span>Career</span><span>Health</span><span>Family</span><span>Finance</span><span>Growth</span></div>
    <svg class="wave" viewBox="0 0 100 30" preserveAspectRatio="none" height="70"><path d="M0 14 Q40 2 100 8 V30 H0Z" fill="var(--blue-light)"/><path d="M0 20 Q45 8 100 12 V30 H0Z" fill="var(--blue-deep)"/></svg>
    <div class="footer">4810 North Calloway Avenue, Suite C 240<br>Missoula, Montana 59417<br>silverheronguidance-example.com</div>
  </section>
</div>

<!-- Letterhead blank -->
<div class="holder" style="left:276px;top:14px;width:235px;height:358px;">
  <div class="label">Letterhead</div>
  <section class="piece" style="inset:0;">
    <div class="brand" style="position:absolute;left:14px;top:18px;font-size:8px;"><span class="brand__dot"></span>Silver Heron<br>Guidance Studio</div>
    <svg class="wave" viewBox="0 0 100 30" preserveAspectRatio="none" height="70"><path d="M0 14 Q40 2 100 8 V30 H0Z" fill="var(--blue-light)"/><path d="M0 20 Q45 8 100 12 V30 H0Z" fill="var(--blue-deep)"/></svg>
    <div class="footer">4810 North Calloway Avenue, Suite C 240<br>Missoula, Montana 59417<br>silverheronguidance-example.com</div>
  </section>
</div>

<!-- Business card front -->
<div class="holder" style="left:540px;top:36px;width:120px;height:72px;">
  <div class="label">Business Card Front</div>
  <section class="piece" style="inset:0;">
    <div class="brand" style="position:absolute;left:10px;top:16px;font-size:6.5px;"><span class="brand__dot"></span>Silver Heron<br>Guidance Studio</div>
    <div class="tagline" style="position:absolute;left:10px;top:40px;color:var(--blue-mid);">Let Your Dreams Take Flight</div>
    <svg class="wave" viewBox="0 0 100 30" preserveAspectRatio="none" height="18"><path d="M0 14 Q40 2 100 8 V30 H0Z" fill="var(--blue-light)"/><path d="M0 20 Q45 8 100 12 V30 H0Z" fill="var(--blue-deep)"/></svg>
  </section>
</div>

<!-- Business card back -->
<div class="holder" style="left:672px;top:36px;width:120px;height:72px;">
  <div class="label">Business Card Back</div>
  <section class="piece piece--blue" style="inset:0;padding:10px;">
    <div style="font-size:6px;font-weight:600;">Marla Penrick, MA</div>
    <div class="small" style="margin-top:6px;">4810 North Calloway Avenue, Suite C 240<br>Missoula, Montana 59417<br>silverheronguidance@mailbox-example.net<br>silverheronguidance-example.com</div>
  </section>
</div>

<!-- Envelope front -->
<div class="holder" style="left:540px;top:132px;width:252px;height:120px;">
  <div class="label">Envelope Front</div>
  <section class="piece" style="inset:0;">
    <div class="brand" style="position:absolute;left:12px;top:12px;font-size:6.5px;"><span class="brand__dot"></span>Silver Heron<br>Guidance Studio</div>
    <div class="small" style="position:absolute;left:12px;top:34px;">4810 North Calloway Avenue<br>Suite C 240<br>Missoula, Montana 59417</div>
    <svg class="wave" viewBox="0 0 100 30" preserveAspectRatio="none" height="34"><path d="M0 14 Q40 2 100 8 V30 H0Z" fill="var(--blue-light)"/><path d="M0 20 Q45 8 100 12 V30 H0Z" fill="var(--blue-deep)"/></svg>
  </section>
</div>

<!-- Envelope back -->
<div class="holder" style="left:540px;top:276px;width:252px;height:96px;">
  <div class="label">Envelope Back</div>
  <section class="piece piece--blue" style="inset:0;">
    <svg class="flap" viewBox="0 0 100 60" preserveAspectRatio="none"><path d="M0 0 L50 55 L100 0Z" fill="var(--blue-pale)"/></svg>
  </section>
</div>

<!-- Post card front -->
<div class="holder" style="left:835px;top:36px;width:154px;height:104px;">
  <div class="label">Post Card Front</div>
  <section class="piece" style="inset:0;">
    <div class="brand" style="position:absolute;left:8px;top:10px;font-size:5.5px;"><span class="brand__dot"></span>Silver Heron<br>Guidance Studio</div>
    <div class="divider"></div>
    <div class="stamp"></div>
    <div class="postlines"><i></i><i></i><i></i></div>
    <svg class="wave" viewBox="0 0 100 30" preserveAspectRatio="none" height="22"><path d="M0 14 Q40 2 100 8 V30 H0Z" fill="var(--blue-light)"/><path d="M0 20 Q45 8 100 12 V30 H0Z" fill="var(--blue-deep)"/></svg>
  </section>
</div>

<!-- Thank you card front -->
<div class="holder" style="left:1003px;top:36px;width:154px;height:104px;">
  <div class="label">Thank You Card</div>
  <section class="piece" style="inset:0;">
    <div class="brand" style="position:absolute;left:8px;top:10px;font-size:5.5px;"><span class="brand__dot"></span>Silver Heron<br>Guidance Studio</div>
    <div class="script" style="position:absolute;right:14px;top:36px;font-size:20px;color:var(--blue-mid);">Thank You</div>
    <svg class="wave" viewBox="0 0 100 30" preserveAspectRatio="none" height="22"><path d="M0 14 Q40 2 100 8 V30 H0Z" fill="var(--blue-light)"/><path d="M0 20 Q45 8 100 12 V30 H0Z" fill="var(--blue-deep)"/></svg>
  </section>
</div>

<!-- Post card back -->
<div class="holder" style="left:835px;top:168px;width:154px;height:96px;">
  <div class="label">Post Card Back</div>
  <section class="piece piece--blue" style="inset:0;">
    <div class="brand brand--white" style="position:absolute;left:48px;top:30px;font-size:6px;"><span class="brand__dot"></span>Silver Heron<br>Guidance Studio</div>
    <div class="small" style="position:absolute;left:0;right:0;bottom:6px;text-align:center;">silverheronguidance-example.com</div>
  </section>
</div>

<!-- Thank you card back -->
<div class="holder" style="left:1003px;top:168px;width:154px;height:96px;">
  <div class="label">Card Back</div>
  <section class="piece piece--blue" style="inset:0;">
    <div class="brand brand--white" style="position:absolute;left:48px;top:30px;font-size:6px;"><span class="brand__dot"></span>Silver Heron<br>Guidance Studio</div>
    <div class="small" style="position:absolute;left:0;right:0;bottom:6px;text-align:center;">silverheronguidance-example.com</div>
  </section>
</div>

</body>
</html>
```